Flyer Design Project

Hi There
Im a Photobooth company called SnapNook Rentals KX, We rent out PhotoBooth for weddings, Parties and Coperate Functions.
im exbiting at an expo and need some flyers to hand out to our potential customer.
The back of the poster should include our pricing and packages.
We looking for an eye catching fyler, that display all information needed for a potential customer to see what service we offer

It Company

```html
<!DOCTYPE html>
<html lang="en">
<head>
<meta charset="utf-8">
<title>SnapNook Rentals KX – Packages</title>
<link href="https://fonts.googleapis.com/css2?family=Fredoka:wght@700&family=Comic+Neue:wght@400;700&family=Roboto+Condensed:wght@700&family=Arimo:wght@400;700&display=swap" rel="stylesheet">
<style>
  :root{
    --sky:#1aa7e8;
    --white:#ffffff;
    --ink:#1a1a1a;
    --grid:#6f6f6f;
    --silver-cell:#e6e6e7;
    --gold-head:#f7a51e;
    --gold-cell:#fdd9a0;
    --plat-head:#161616;
    --plat-cell:#9d9d9f;
  }
  *{box-sizing:border-box;margin:0;padding:0}
  html,body{width:848px;height:1200px;overflow:hidden;background:var(--white)}
  .flyer{position:relative;width:848px;height:1200px;background:var(--white);color:var(--ink)}
  .intro-band{position:absolute;left:0;top:0;width:848px;height:134px;background:var(--sky);
    display:flex;align-items:center;justify-content:center;text-align:center}
  .intro-band h1{font-family:"Fredoka",sans-serif;font-weight:700;color:var(--white);
    font-size:29px;line-height:40px;letter-spacing:.2px}
  .packages{position:absolute;left:72px;top:160px;width:706px;border-collapse:collapse;table-layout:fixed}
  .packages td,.packages th{border:1px solid var(--grid);height:51.3px}
  .packages col.feature{width:392px}
  .packages col.silver{width:107px}
  .packages col.gold{width:103px}
  .packages col.platinum{width:104px}
  .packages thead th{height:53px;font-family:"Roboto Condensed",sans-serif;font-weight:700;font-size:21px;text-align:center}
  .packages thead th.feature{background:var(--white);color:var(--ink)}
  .packages thead th.silver{background:linear-gradient(90deg,#ffffff,#bdbdbf)}
  .packages thead th.gold{background:linear-gradient(90deg,#fff4d9,var(--gold-head) 70%)}
  .packages thead th.platinum{background:linear-gradient(90deg,#7a7a7a,var(--plat-head) 60%);color:var(--white)}
  .packages td.feature{font-family:"Comic Neue",sans-serif;font-size:19px;line-height:20px;padding:2px 8px}
  .packages td.silver{background:var(--silver-cell)}
  .packages td.gold{background:var(--gold-cell)}
  .packages td.platinum{background:var(--plat-cell)}
  .packages td.mark{text-align:center}
  .tick{width:30px;height:30px;display:inline-block;vertical-align:middle}
  .packages tr.prices td{height:52px;font-family:"Roboto Condensed",sans-serif;font-weight:700;font-size:26px;padding-left:8px}
  .extras{position:absolute;left:79px;top:904px;font-family:"Arimo",sans-serif;font-weight:700;font-size:22px}
  .terms{position:absolute;left:82px;top:962px;width:452px;font-family:"Arimo",sans-serif;font-size:15.5px;line-height:19px}
  .brand{position:absolute;left:82px;top:1100px;font-family:"Arimo",sans-serif;font-weight:700;
    font-size:38px;line-height:44px;color:var(--sky)}
  .booth{position:absolute;left:612px;top:954px;width:128px;height:228px;
    background:linear-gradient(180deg,#2a2a2a,#0d0d0d)}
</style>
</head>
<body>
<svg width="0" height="0" style="position:absolute">
  <defs>
    <symbol id="tick" viewBox="0 0 30 30">
      <path d="M3 16 L7 13 L12 20 C16 12 21 6 27 2 L28 4 C22 9 17 16 12 27 Z" fill="#1a1a1a"/>
    </symbol>
  </defs>
</svg>
<div class="flyer">
  <header class="intro-band">
    <h1>Below are the packages we offer, these have been<br>carefully crafted to suit everyones needs and budget!</h1>
  </header>

  <table class="packages">
    <colgroup><col class="feature"><col class="silver"><col class="gold"><col class="platinum"></colgroup>
    <thead>
      <tr><th class="feature">Package</th><th class="silver">Silver</th><th class="gold">Gold</th><th class="platinum">Platinum</th></tr>
    </thead>
    <tbody>
      <tr><td class="feature">4 hours of unlimited photos</td>
        <td class="silver mark"><svg class="tick"><use href="#tick"/></svg></td>
        <td class="gold mark"><svg class="tick"><use href="#tick"/></svg></td>
        <td class="platinum mark"></td></tr>
      <tr><td class="feature">6 hours of unlimited photos</td>
        <td class="silver mark"></td><td class="gold mark"></td>
        <td class="platinum mark"><svg class="tick"><use href="#tick"/></svg></td></tr>
      <tr><td class="feature">Black &amp; White, Color and Sepia photos</td>
        <td class="silver mark"><svg class="tick"><use href="#tick"/></svg></td>
        <td class="gold mark"><svg class="tick"><use href="#tick"/></svg></td>
        <td class="platinum mark"><svg class="tick"><use href="#tick"/></svg></td></tr>
      <tr><td class="feature">Total customization of strips<br>(names, dates or personalized graphics)</td>
        <td class="silver mark"><svg class="tick"><use href="#tick"/></svg></td>
        <td class="gold mark"><svg class="tick"><use href="#tick"/></svg></td>
        <td class="platinum mark"><svg class="tick"><use href="#tick"/></svg></td></tr>
      <tr><td class="feature">Hassel free delivery, setup and removal</td>
        <td class="silver mark"><svg class="tick"><use href="#tick"/></svg></td>
        <td class="gold mark"><svg class="tick"><use href="#tick"/></svg></td>
        <td class="platinum mark"><svg class="tick"><use href="#tick"/></svg></td></tr>
      <tr><td class="feature">The Prop Box<br>(glasses, wigs, boas, hats, masks, etc)</td>
        <td class="silver mark"><svg class="tick"><use href="#tick"/></svg></td>
        <td class="gold mark"><svg class="tick"><use href="#tick"/></svg></td>
        <td class="platinum mark"><svg class="tick"><use href="#tick"/></svg></td></tr>
      <tr><td class="feature">A Guestbook to create a<br>&nbsp;one-of-a-kind masterpiece</td>
        <td class="silver mark"></td>
        <td class="gold mark"><svg class="tick"><use href="#tick"/></svg></td>
        <td class="platinum mark"><svg class="tick"><use href="#tick"/></svg></td></tr>
      <tr><td class="feature">Copyright-free DVD of ALL<br>Pictures and/or Videos</td>
        <td class="silver mark"></td>
        <td class="gold mark"><svg class="tick"><use href="#tick"/></svg></td>
        <td class="platinum mark"><svg class="tick"><use href="#tick"/></svg></td></tr>
      <tr><td class="feature">Allow guests to email photo’s to<br>themselves</td>
        <td class="silver mark"><svg class="tick"><use href="#tick"/></svg></td>
        <td class="gold mark"><svg class="tick"><use href="#tick"/></svg></td>
        <td class="platinum mark"><svg class="tick"><use href="#tick"/></svg></td></tr>
      <tr><td class="feature">Guests can instantly upload photos to<br>FRAMESHARE!!!</td>
        <td class="silver mark"></td><td class="gold mark"></td>
        <td class="platinum mark"><svg class="tick"><use href="#tick"/></svg></td></tr>
      <tr><td class="feature">Unlimited extra copies of strips and<br>6x4 Prints of guest best shots</td>
        <td class="silver mark"></td><td class="gold mark"></td>
        <td class="platinum mark"><svg class="tick"><use href="#tick"/></svg></td></tr>
      <tr><td class="feature">Video Messages</td>
        <td class="silver mark"></td><td class="gold mark"></td>
        <td class="platinum mark"><svg class="tick"><use href="#tick"/></svg></td></tr>
      <tr class="prices"><td class="feature">Prices</td>
        <td class="silver">$1200</td><td class="gold">$1400</td><td class="platinum">$1700</td></tr>
    </tbody>
  </table>

  <p class="extras">Additional Extras: Additional hours - $200,&nbsp; Idle Hours - $50</p>

  <p class="terms">Please note, these prices are only valid for private functions on Friday evenings and all day Saturday/Sunday. Not vaid on Public Holidays or Long weekends. For other fuctions please contact us for a quote.</p>

  <p class="brand">SnapNook Rentals KX</p>

  <div class="booth" role="img" aria-label="Photo of a black enclosed photo booth kiosk with curtain"></div>
</div>
</body>
</html>
```